NEW Modern Sleek Business Card for VR Language Startup

Our startup is using VR to lead the next wave of world language education. We need a two-sided business card that introduces the larger organization (Quorvel Language Inc) and our contact info on one side and shows the product, Lumidrasca, on the other side.

Side 1 (contact info)= Quorvel Logo and Contact info (name, title, phone, email)

Side 2 (product)= Lumidrasc logo, text, and website
Text= Culturally Immersive Language Learning Games
Website= www.lumidrasc.example

Target Market(s)

Education, Technology

Contact Information for Business Card

Contact info will be updated upon approval of the design. For now, put this as a placeholder.

Perry Hollins
Founder & CEO
phollins@mailtrove.example
(555)-014-2736

Font styles to use
Other font styles liked:
• Gibson and Century Gothic are the brand fonts

Requirements
Nice to have
• I would love to see cohesion between the design and colors of the two logos. I have attached a few business card designs that I like, so you can get a feel for my preferred style.

```html
<!DOCTYPE html>
<html lang="en">
<head>
<meta charset="utf-8">
<title>Quorvel Language – Business Card</title>
<link rel="stylesheet" href="https://fonts.googleapis.com/css2?family=Montserrat:wght@400;500;600;700&family=Questrial&display=swap">
<style>
  :root{
    --page:#2b2b2d;
    --card:#ffffff;
    --ink:#2a2a2e;
    --muted:#6d6d72;
    --rule:#555559;
    --cyan:#33c3e3;
    --blue:#4a86d8;
    --indigo:#5a63c9;
    --orange:#f5843a;
    --red:#ee4a64;
    --magenta:#c23d8e;
    --purple:#8e4bb8;
  }
  *{box-sizing:border-box;margin:0;padding:0}
  html,body{width:1200px;height:900px;overflow:hidden;background:var(--page)}
  body{position:relative;font-family:"Montserrat",sans-serif;color:var(--ink)}

  .card{position:absolute;left:240px;width:720px;height:400px;background:var(--card);overflow:hidden;box-shadow:0 10px 30px rgba(0,0,0,.45)}
  .card--product{top:30px}
  .card--contact{top:470px}

  .pattern{position:absolute;left:0;right:0}
  .pattern--top{top:0;height:120px;-webkit-mask-image:linear-gradient(to bottom,#000 0%,rgba(0,0,0,.15) 100%);mask-image:linear-gradient(to bottom,#000 0%,rgba(0,0,0,.15) 100%)}
  .pattern--bottom{bottom:0;height:130px;-webkit-mask-image:linear-gradient(to top,#000 0%,rgba(0,0,0,.15) 100%);mask-image:linear-gradient(to top,#000 0%,rgba(0,0,0,.15) 100%)}
  .card--product .pattern--top{background:linear-gradient(90deg,var(--cyan) 0%,var(--cyan) 45%,var(--blue) 80%,var(--indigo) 100%);opacity:.8}
  .card--product .pattern--bottom{background:linear-gradient(90deg,var(--cyan) 0%,var(--cyan) 50%,var(--blue) 80%,var(--indigo) 100%);opacity:.8}
  .card--contact .pattern--top{background:linear-gradient(90deg,var(--orange) 0%,var(--red) 35%,var(--magenta) 65%,var(--purple) 100%);opacity:.8}
  .card--contact .pattern--bottom{background:linear-gradient(90deg,var(--orange) 0%,var(--red) 30%,var(--magenta) 55%,var(--purple) 75%,var(--blue) 100%);opacity:.8}

  .content{position:absolute;top:120px;bottom:130px;left:0;right:0;display:flex;align-items:center}
  .brand{display:flex;align-items:center;gap:14px;flex:none}
  .brand__dot{width:58px;height:58px;border-radius:50%;flex:none}
  .brand__name{font-family:"Questrial",sans-serif;font-size:38px;color:var(--muted);letter-spacing:.5px;white-space:nowrap}
  .divider{flex:none;width:2px;height:110px;background:var(--rule);margin:0 34px}

  .card--product .content{padding-left:120px}
  .card--product .brand__dot{background:var(--blue)}
  .tagline{font-size:17px;font-weight:500;color:var(--muted);line-height:1.2;width:220px}
  .website{margin-top:10px;font-size:17px;font-weight:600;color:var(--cyan);white-space:nowrap}

  .card--contact .content{padding-left:56px}
  .card--contact .brand{gap:12px}
  .card--contact .brand__dot{width:54px;height:54px;background:var(--red)}
  .card--contact .brand__name{font-family:"Montserrat",sans-serif;font-weight:600;font-size:30px;letter-spacing:5px;color:var(--ink)}
  .card--contact .divider{margin:0 26px}
  .person{flex:none;white-space:nowrap}
  .person__name{font-size:22px;font-weight:700;letter-spacing:.5px;background:linear-gradient(90deg,var(--orange),var(--magenta) 60%,var(--purple));-webkit-background-clip:text;background-clip:text;color:transparent}
  .person__title{font-size:16px;font-weight:500;color:var(--ink);margin-top:2px}
  .contact-list{list-style:none;margin-top:10px}
  .contact-list li{display:flex;align-items:center;gap:9px;font-size:16px;font-weight:500;line-height:1.5}
  .contact-list svg{width:16px;height:16px;flex:none}
</style>
</head>
<body>

<section class="card card--product" aria-label="Product side">
  <div class="pattern pattern--top" role="img" aria-label="Scattered blue pixel-square pattern"></div>
  <div class="content">
    <div class="brand">
      <span class="brand__dot"></span>
      <span class="brand__name">Lumidrasc</span>
    </div>
    <span class="divider"></span>
    <div>
      <p class="tagline">Culturally Immersive Language Learning Games</p>
      <p class="website">www.lumidrasc.example</p>
    </div>
  </div>
  <div class="pattern pattern--bottom" role="img" aria-label="Scattered cyan to indigo pixel-square pattern"></div>
</section>

<section class="card card--contact" aria-label="Contact side">
  <div class="pattern pattern--top" role="img" aria-label="Scattered orange to purple pixel-square pattern"></div>
  <div class="content">
    <div class="brand">
      <span class="brand__dot"></span>
      <span class="brand__name">QUORVEL</span>
    </div>
    <span class="divider"></span>
    <div class="person">
      <p class="person__name">PERRY HOLLINS</p>
      <p class="person__title">Founder &amp; CEO</p>
      <ul class="contact-list">
        <li>
          <svg viewBox="0 0 24 24" aria-hidden="true"><path fill="#f5843a" d="M6.6 10.8a15.1 15.1 0 0 0 6.6 6.6l2.2-2.2a1 1 0 0 1 1-.25 11.4 11.4 0 0 0 3.6.57 1 1 0 0 1 1 1V20a1 1 0 0 1-1 1A17 17 0 0 1 3 4a1 1 0 0 1 1-1h3.5a1 1 0 0 1 1 1c0 1.25.2 2.45.57 3.57a1 1 0 0 1-.25 1z"/></svg>
          (555)-014-2736
        </li>
        <li>
          <svg viewBox="0 0 24 24" aria-hidden="true"><rect x="2" y="5" width="20" height="14" rx="1.5" fill="#ee4a64"/><path d="M3 6.5l9 6.5 9-6.5" fill="none" stroke="#fff" stroke-width="1.8"/></svg>
          phollins@mailtrove.example
        </li>
      </ul>
    </div>
  </div>
  <div class="pattern pattern--bottom" role="img" aria-label="Scattered orange, magenta, purple and blue pixel-square pattern"></div>
</section>

</body>
</html>
```